Q-Forma Stationary Package
Nimble Forma
Q-Forma Stationary Package - Internet Services
Creative Brief
Professional
Tom Gaskin
President and CEO
P.O. Box 4352 Burlington, NJ 08016
Tom.Gaskin@Q-FormaLLC.example
www.Q-FormaLLC.example
I am interested in seeing business card designs in both horizontal and vertical styles. My company provided technical consulting for the PGB Veterans, KRTU, KRTU Sergeants, KRTU Lieutenants and Halvern PD Senior Officers’ Association. I would like their logos on my card either on the front or the back listed under the words "Technical Consulting." You can find their logos located at https://www.filevault.example/s/83k2m1q7zpwe4tx/consulting.zip?dl=0. Unfortunately, some of these logos are only available from me in low-resolution.

```html
<!DOCTYPE html>
<html lang="en">
<head>
<meta charset="utf-8">
<title>Q-Forma Business Card</title>
<link rel="stylesheet" href="https://fonts.googleapis.com/css2?family=Montserrat:wght@400;600;700;800&family=Open+Sans:wght@400;600&display=swap">
<style>
  :root {
    --page-bg: #e9ebee;
    --card-white: #ffffff;
    --brand-blue: #1e9fd8;
    --brand-blue-dark: #1685c0;
    --brand-blue-light: #7fcdf0;
    --swoosh-grey: #b9bec4;
    --text-dark: #3f4347;
    --text-mid: #6b7076;
    --rule-grey: #c9cdd1;
  }
  * { box-sizing: border-box; margin: 0; padding: 0; }
  html, body { width: 1200px; height: 901px; overflow: hidden; }
  body {
    background: var(--page-bg);
    font-family: "Open Sans", Arial, sans-serif;
    position: relative;
  }
  .business-card {
    position: absolute;
    left: 100px; top: 165px;
    width: 1000px; height: 572px;
    background: var(--card-white);
    border-radius: 34px;
    overflow: hidden;
    box-shadow: 0 10px 30px rgba(0,0,0,0.12);
  }
  .card-waves { position: absolute; left: 0; top: 0; width: 1000px; height: 572px; }
  .brand-block {
    position: absolute; left: 70px; top: 200px; width: 330px;
  }
  .brand-name {
    display: flex; align-items: center; gap: 14px;
    font-family: "Montserrat", Arial, sans-serif;
    font-weight: 800; font-size: 62px; line-height: 1;
    color: var(--brand-blue);
  }
  .brand-mark {
    width: 26px; height: 26px; border-radius: 50%;
    background: var(--brand-blue);
  }
  .brand-tagline {
    margin-top: 10px;
    font-size: 12.5px; color: var(--brand-blue-dark);
    letter-spacing: 0.2px;
  }
  .divider {
    position: absolute; left: 455px; top: 50px;
    width: 1px; height: 300px; background: var(--rule-grey);
  }
  .contact-block {
    position: absolute; left: 480px; top: 58px; width: 460px;
  }
  .person-name {
    font-family: "Montserrat", Arial, sans-serif;
    font-weight: 600; font-size: 21px; letter-spacing: 1.5px;
    color: var(--brand-blue); text-transform: uppercase;
  }
  .person-role { font-size: 15px; color: var(--text-mid); margin-top: 2px; }
  .address { margin-top: 26px; font-size: 15px; line-height: 1.4; color: var(--text-dark); }
  .contact-list { list-style: none; margin-top: 20px; }
  .contact-list li {
    display: flex; align-items: center; gap: 12px;
    font-size: 14px; color: var(--text-dark); height: 26px;
  }
  .contact-icon { width: 17px; height: 17px; flex: none; }
</style>
</head>
<body>
  <article class="business-card">
    <svg class="card-waves" viewBox="0 0 1000 572" aria-hidden="true">
      <path d="M0 440 C 280 420, 640 400, 1000 290 L1000 316 C 640 425, 300 448, 0 470 Z" fill="var(--swoosh-grey)"/>
      <path d="M0 478 C 320 458, 660 430, 1000 330 L1000 412 C 660 500, 320 512, 0 520 Z" fill="var(--brand-blue)"/>
      <path d="M0 520 C 320 512, 660 500, 1000 412 L1000 430 C 660 520, 320 528, 0 534 Z" fill="var(--brand-blue-light)"/>
      <path d="M0 548 C 340 540, 680 528, 1000 470 L1000 572 L0 572 Z" fill="#eef0f2"/>
    </svg>

    <div class="brand-block">
      <div class="brand-name"><span class="brand-mark"></span>Q-Forma</div>
      <p class="brand-tagline">Delivering smart solutions for every technology need</p>
    </div>

    <div class="divider"></div>

    <section class="contact-block">
      <h1 class="person-name">Ethan Caldwell</h1>
      <p class="person-role">Managing Director</p>
      <p class="address">412 9th Cedar Mall<br>Harbor Road LKN</p>
      <ul class="contact-list">
        <li>
          <svg class="contact-icon" viewBox="0 0 20 20"><circle cx="10" cy="10" r="10" fill="var(--brand-blue)"/><path d="M6.5 5.5 l2 0 l1 2.5 l-1.3 1 a6 6 0 0 0 2.8 2.8 l1-1.3 l2.5 1 l0 2 a1 1 0 0 1 -1 1 a8.5 8.5 0 0 1 -8-8 a1 1 0 0 1 1-1z" fill="#fff"/></svg>
          010 555 0142
        </li>
        <li>
          <svg class="contact-icon" viewBox="0 0 20 20"><circle cx="10" cy="10" r="10" fill="var(--brand-blue)"/><rect x="5" y="6" width="10" height="8" rx="1" fill="#fff"/><rect x="7" y="8" width="6" height="2" fill="var(--brand-blue)"/></svg>
          010 555 0143
        </li>
        <li>
          <svg class="contact-icon" viewBox="0 0 20 20"><circle cx="10" cy="10" r="10" fill="var(--brand-blue)"/><rect x="7" y="4.5" width="6" height="11" rx="1.2" fill="#fff"/><circle cx="10" cy="13.5" r="0.8" fill="var(--brand-blue)"/></svg>
          010 555 0144
        </li>
        <li>
          <svg class="contact-icon" viewBox="0 0 20 20"><circle cx="10" cy="10" r="10" fill="var(--brand-blue)"/><rect x="5" y="6.5" width="10" height="7" fill="#fff"/><path d="M5 6.5 L10 10.5 L15 6.5" stroke="var(--brand-blue)" stroke-width="1.1" fill="none"/></svg>
          mail@nimbleforma.example
        </li>
        <li>
          <svg class="contact-icon" viewBox="0 0 20 20"><circle cx="10" cy="10" r="10" fill="var(--brand-blue)"/><circle cx="10" cy="10" r="5" fill="none" stroke="#fff" stroke-width="1.2"/><path d="M5 10 H15 M10 5 C 7.5 8, 7.5 12, 10 15 M10 5 C 12.5 8, 12.5 12, 10 15" stroke="#fff" stroke-width="1" fill="none"/></svg>
          www.nimbleforma.example
        </li>
      </ul>
    </section>
  </article>
</body>
</html>
```